Professional Services (B-2-B) Business Cards (Front & Back)

Quintarion is a business-to-business professional services company in the legal sector. They typically present to c-suite and executive functions who are looking for providers with expertise, and experience. Our business card should look and feel professional and contemporary, but we are not a startup tech company, so we want the tone to be more mature.

```html
<!DOCTYPE html>
<html lang="en">
<head>
<meta charset="utf-8">
<title>Quintarion Business Cards</title>
<link href="https://fonts.googleapis.com/css2?family=Montserrat:wght@400;500;700;800&display=swap" rel="stylesheet">
<style>
  :root {
    --stage: #c9cbcf;
    --navy-deep: #0b1f4d;
    --navy: #0f2a66;
    --navy-bright: #123a8f;
    --navy-edge: #2f6fc4;
    --ink: #0f2350;
    --ink-soft: #55617a;
    --paper: #ffffff;
  }
  * { box-sizing: border-box; margin: 0; padding: 0; }
  html, body { width: 1200px; height: 800px; overflow: hidden; }
  body {
    background: linear-gradient(160deg, #dedfe2 0%, var(--stage) 60%, #b9bbbf 100%);
    font-family: "Montserrat", Arial, sans-serif;
    display: flex;
    align-items: center;
    justify-content: center;
    gap: 40px;
  }
  .card {
    width: 540px;
    height: 309px;
    position: relative;
    overflow: hidden;
    border-bottom: 3px solid var(--navy-edge);
    box-shadow: 0 18px 36px rgba(0, 0, 0, 0.28);
  }

  /* Contact side */
  .card--contact { display: flex; }
  .contact__brand {
    width: 54%;
    background: linear-gradient(150deg, var(--navy) 0%, var(--navy-deep) 100%);
    display: flex;
    align-items: center;
    justify-content: center;
    gap: 12px;
  }
  .contact__details {
    width: 46%;
    background: var(--paper);
    padding: 70px 20px 0 30px;
  }
  .brand-mark {
    width: 14px;
    height: 14px;
    background: var(--paper);
  }
  .brand-name {
    color: var(--paper);
    font-weight: 500;
    letter-spacing: 0.32em;
    text-transform: uppercase;
  }
  .contact__brand .brand-name { font-size: 17px; }
  .person-name {
    color: var(--ink);
    font-weight: 800;
    font-size: 20px;
    letter-spacing: 0.02em;
    text-transform: uppercase;
  }
  .person-title {
    color: var(--ink-soft);
    font-size: 11.5px;
    margin-top: 2px;
  }
  .contact-list {
    list-style: none;
    margin-top: 20px;
  }
  .contact-list li {
    display: flex;
    align-items: center;
    gap: 8px;
    color: var(--ink-soft);
    font-size: 11.5px;
    margin-bottom: 6px;
  }
  .contact-icon { width: 16px; height: 16px; flex: none; }

  /* Logo side */
  .card--logo {
    background: linear-gradient(100deg, var(--navy-deep) 0%, var(--navy) 45%, var(--navy-bright) 100%);
    display: flex;
    align-items: center;
    justify-content: center;
    gap: 16px;
  }
  .logo__backdrop {
    position: absolute;
    inset: 0;
    background:
      linear-gradient(180deg, rgba(255,255,255,0) 20%, rgba(70,120,220,0.18) 45%, rgba(255,255,255,0) 60%),
      linear-gradient(180deg, rgba(0,0,0,0) 60%, rgba(5,15,45,0.45) 100%);
  }
  .card--logo .brand-mark { width: 20px; height: 20px; position: relative; }
  .card--logo .brand-name { font-size: 30px; position: relative; }
</style>
</head>
<body>

  <section class="card card--contact" aria-label="Business card, contact side">
    <div class="contact__brand">
      <span class="brand-mark"></span>
      <span class="brand-name">Quintarion</span>
    </div>
    <div class="contact__details">
      <h1 class="person-name">Mark Ellison</h1>
      <p class="person-title">President &amp; CEO</p>
      <ul class="contact-list">
        <li>
          <svg class="contact-icon" viewBox="0 0 16 16" aria-hidden="true">
            <circle cx="8" cy="8" r="8" fill="#0f2350"/>
            <path d="M5.2 4.3l1.4-.3.8 1.9-.9.7c.5 1 1.3 1.8 2.3 2.3l.7-.9 1.9.8-.3 1.4c-3.4.2-6.1-2.5-5.9-5.9z" fill="#fff"/>
          </svg>
          (415) 555-0148
        </li>
        <li>
          <svg class="contact-icon" viewBox="0 0 16 16" aria-hidden="true">
            <circle cx="8" cy="8" r="8" fill="#0f2350"/>
            <rect x="5.5" y="3.8" width="5" height="8.4" rx="0.8" fill="none" stroke="#fff" stroke-width="1"/>
          </svg>
          (203) 555-0172
        </li>
        <li>
          <svg class="contact-icon" viewBox="0 0 16 16" aria-hidden="true">
            <circle cx="8" cy="8" r="8" fill="#0f2350"/>
            <rect x="4" y="5" width="8" height="6" fill="none" stroke="#fff" stroke-width="1"/>
            <path d="M4 5l4 3.2L12 5" fill="none" stroke="#fff" stroke-width="1"/>
          </svg>
          mellison@quintarion.tech
        </li>
        <li>
          <svg class="contact-icon" viewBox="0 0 16 16" aria-hidden="true">
            <circle cx="8" cy="8" r="8" fill="#0f2350"/>
            <circle cx="8" cy="8" r="4" fill="none" stroke="#fff" stroke-width="1"/>
            <path d="M4 8h8M8 4c-1.6 1.8-1.6 6.2 0 8M8 4c1.6 1.8 1.6 6.2 0 8" fill="none" stroke="#fff" stroke-width="0.8"/>
          </svg>
          www.quintarion.tech
        </li>
      </ul>
    </div>
  </section>

  <section class="card card--logo" aria-label="Business card, logo side">
    <div class="logo__backdrop" role="img" aria-label="Abstract blurred blue light streaks in deep navy tones"></div>
    <span class="brand-mark"></span>
    <span class="brand-name">Quintarion</span>
  </section>

</body>
</html>
```